Business card design needed

Our company background is that we provides transfers to and from the airport, social & corporate events, weddings.
We are also available for charter for birthday party, wine tastings, concerts, anniversary, school balls etc.
Our business cards have to reflect that we have a professional company, they are our first contact and have to stand out from the other 'players' in the market.

Industry/Entity Type

School

Contact Information for Business Card

BRISTEL QDF, Laurent & Marisol, mob: 0427 381 594, PO Box 287, Tarrowin WA 6311, ABN 52 914 603 278, Lic 7169/5804,

Requirements
Must have
• Telephone number: 0427 381 594
Website: www.BRISTELQDF.com.au
postal address: PO Box 287, Tarrowin WA 6311
Licences: Lic 7169/5804

***If using the new photo (one with the bus and buildings behind it), if possible can the buildings be cropped out. Thanks
Nice to have
• would be nice to have the pics of the vehicle(s), preferred the Pel on the card but not too fussed.
Should not have
• Picture of vehicle we don't have in our fleet. (We ONLY have the Pellics and Rendak Ovaro mini bus)

```html
<!DOCTYPE html>
<html lang="en">
<head>
<meta charset="utf-8">
<title>Bristel QDF – Business Card</title>
<link rel="stylesheet" href="https://fonts.googleapis.com/css2?family=Arimo:wght@400&family=Tinos:wght@400&family=Luckiest+Guy&display=swap">
<style>
  :root {
    --bg-top: #2a2a2a;
    --bg-bottom: #050505;
    --card-white: #ffffff;
    --ink: #1b1b1b;
    --brand-grey: #8a8a8a;
    --rule: #222222;
    --promo-yellow: #fff200;
    --promo-band: rgba(40, 40, 40, 0.88);
    --photo-sky: #dfe6ea;
    --photo-tree: #4f6b3a;
    --photo-road: #7d7a74;
    --photo-silver: #b9b7b2;
    --van-white: #f3f4f5;
  }
  * { box-sizing: border-box; margin: 0; padding: 0; }
  html, body { width: 1200px; height: 900px; overflow: hidden; }
  body {
    background: linear-gradient(180deg, var(--bg-top) 0%, var(--bg-bottom) 100%);
    position: relative;
  }
  .card {
    position: absolute;
    top: 295px;
    width: 520px;
    height: 310px;
    overflow: hidden;
    background: var(--card-white);
    box-shadow: 0 10px 30px rgba(0,0,0,0.6);
  }
  .card--front { left: 60px; }
  .card--back { left: 620px; }

  /* front */
  .front-header {
    position: absolute; inset: 0 0 auto 0; height: 122px;
    background: linear-gradient(180deg, #ffffff 0%, #f4f4f4 100%);
  }
  .brand {
    position: absolute; left: 24px; top: 26px;
    font-family: "Tinos", serif;
    color: var(--brand-grey);
    white-space: nowrap;
  }
  .brand__name { font-size: 34px; line-height: 1; letter-spacing: 1px; }
  .brand__tagline { font-size: 17px; margin: 12px 0 0 64px; }
  .contact {
    position: absolute; left: 288px; top: 10px;
    border-left: 1px solid var(--rule);
    padding-left: 8px;
    font-family: "Arimo", sans-serif;
    font-size: 11.5px; line-height: 16.5px; color: var(--ink);
    list-style: none;
    white-space: nowrap;
  }
  .front-photo {
    position: absolute; left: 0; right: 0; bottom: 0; height: 188px;
    background:
      radial-gradient(ellipse 60% 55% at 50% 55%, var(--photo-silver) 0%, #9d9b96 55%, transparent 75%),
      linear-gradient(180deg, #cfd6cf 0%, var(--photo-tree) 14%, #6b8a45 30%, var(--photo-road) 62%, #8a5a44 100%);
  }

  /* back */
  .back-photo {
    position: absolute; inset: 0;
    background:
      radial-gradient(ellipse 58% 45% at 55% 45%, var(--van-white) 0%, #e6e8ea 60%, transparent 78%),
      linear-gradient(180deg, var(--photo-sky) 0%, var(--photo-tree) 22%, #5c7445 45%, var(--photo-road) 80%, #9a9893 100%);
  }
  .back-brand__disc {
    position: absolute; left: 172px; top: 48px;
    width: 112px; height: 112px; border-radius: 50%;
    background: rgba(255,255,255,0.55);
  }
  .back-brand {
    position: absolute; left: 172px; top: 74px;
    font-family: "Tinos", serif; color: var(--brand-grey);
    white-space: nowrap;
  }
  .back-brand__name { display: block; font-size: 22px; line-height: 1; letter-spacing: 1px; }
  .back-brand__tagline { display: block; font-size: 11px; margin: 6px 0 0 28px; }
  .promo {
    position: absolute; left: 0; right: 0; top: 160px; height: 72px;
    background: var(--promo-band);
    display: flex; align-items: center; justify-content: center;
    font-family: "Luckiest Guy", "Arial Black", sans-serif;
    text-transform: uppercase;
    color: var(--promo-yellow);
    font-size: 21px; line-height: 27px; letter-spacing: 1px;
    text-align: center;
    white-space: nowrap;
  }
</style>
</head>
<body>

<section class="card card--front" aria-label="Business card front">
  <div class="front-header">
    <div class="brand">
      <p class="brand__name">BRISTEL QDF</p>
      <p class="brand__tagline">Luxury Car&amp;Coach</p>
    </div>
    <ul class="contact">
      <li>BRISTEL QDF, Laurent &amp; Marisol,</li>
      <li>mob: 0427 381 594, PO Box 287</li>
      <li>Tarrowin WA 6311</li>
      <li>ABN 52 914 603 278</li>
      <li>Lic 7169/5804</li>
      <li>www.BRISTELQDF.com.au</li>
    </ul>
  </div>
  <div class="front-photo" role="img" aria-label="Photo of the front of a silver Pellics luxury sedan parked on a kerb with grass and road behind"></div>
</section>

<section class="card card--back" aria-label="Business card back">
  <div class="back-photo" role="img" aria-label="Photo of a white Rendak Ovaro mini bus parked in front of trees"></div>
  <div class="back-brand__disc"></div>
  <div class="back-brand">
    <span class="back-brand__name">BRISTEL QDF</span>
    <span class="back-brand__tagline">Luxury Car&amp;Coach</span>
  </div>
  <p class="promo">Tell a friend and we will reward<br>you with 5% off your next trip.</p>
</section>

</body>
</html>
```